Halvren Tax Advisers Business Card

We are seeking a clean, professional, and modern double sided business card design for Halvren Tax Advisers, a tax, accounting, and advisory firm serving business owners, professionals, and investors.
The design should convey credibility, precision, trust, and sophistication appropriate for a CPA level tax advisory firm. Avoid playful, trendy, or overly decorative styles. The look should be sharp, balanced, and timeless.
Our official company logo has been uploaded, which must be incorporated appropriately and consistently with the brand. Designers should not modify, distort, or recreate the logo.
Card format
Standard US business card size (3.5 x 2 inches)
Double sided
Design direction
Professional and modern
Minimalist and uncluttered
Strong typography and clean spacing
Subtle visual interest is welcome, but simplicity is preferred
High contrast and readability are critical
Front side
Primary focus on the Halvren Tax Advisers logo
The firm name should be clearly legible and visually prominent
Background may be white or dark, depending on what best complements the logo
Back side
Contact information layout, such as
Name: Martin G. Pellow, MST, CPA, PFS
Title: Managing Director, Tax
Email: mpellow@myhalvrenfirm.net
Website: www.halvrenfirm-example.tax
Mobile: (505) 555-0132
Direct: (575) 555-0187
Main: (575) 555-0149
Address: 3807 Fenwick Rd., Suite 118, Marlow Springs, NM 87199
Icons may be used sparingly if they enhance clarity
The layout should feel organized and structured
Color and style
Use colors that complement the uploaded logo
Neutral, professional tones preferred
Avoid loud or saturated colors
The design should print well on standard cardstock
Print considerations
Design should be print‑ready
No edge to edge elements that risk being cut off
Proper margins and bleed awareness
Overall, the goal is a polished, high end business card that reflects trust, expertise, and professionalism consistent with a firm providing tax strategy, compliance, and advisory services.

```html
<!DOCTYPE html>
<html lang="en">
<head>
<meta charset="utf-8">
<title>Halvren Tax Advisers – Business Card</title>
<link href="https://fonts.googleapis.com/css2?family=Montserrat:wght@300;400;700&display=swap" rel="stylesheet">
<style>
  :root {
    --navy: #1f2757;
    --orange: #e8782e;
    --ink-soft: #55585f;
    --card: #ffffff;
    --card-shade: #eeeeef;
    --backdrop: #2b2b2d;
  }
  * { box-sizing: border-box; margin: 0; padding: 0; }
  html, body {
    width: 1200px; height: 900px; overflow: hidden;
    background: var(--backdrop);
    font-family: "Montserrat", Arial, sans-serif;
  }
  .sheet {
    width: 1200px; height: 900px;
    display: flex; flex-direction: column;
    align-items: center; justify-content: center; gap: 60px;
  }
  .card {
    position: relative;
    width: 630px; height: 360px;
    background: linear-gradient(120deg, var(--card-shade) 0%, var(--card) 55%, var(--card-shade) 100%);
    box-shadow: 0 14px 30px rgba(0,0,0,.45);
  }

  .wordmark {
    color: var(--navy);
    font-weight: 700;
    text-transform: uppercase;
    letter-spacing: .12em;
    white-space: nowrap;
  }

  .card--contact .wordmark {
    position: absolute; top: 42px; right: 40px;
    font-size: 20px;
  }
  .identity {
    position: absolute; top: 128px; left: 40px; right: 40px;
  }
  .identity__name {
    color: var(--navy); font-weight: 700; font-size: 17px;
    text-transform: uppercase; letter-spacing: .01em;
  }
  .identity__row {
    display: flex; align-items: center; gap: 12px; margin-top: 4px;
  }
  .identity__title {
    color: var(--orange); font-weight: 400; font-size: 14px; white-space: nowrap;
  }
  .identity__rule {
    flex: 1; height: 1px; background: var(--orange);
  }
  .contacts {
    position: absolute; left: 40px; top: 210px;
    list-style: none;
  }
  .contacts li {
    display: flex; align-items: center; gap: 10px;
    color: var(--ink-soft); font-weight: 300; font-size: 13.5px;
    line-height: 24px;
  }
  .contacts svg { width: 13px; height: 13px; fill: var(--navy); flex: none; }
  .address {
    position: absolute; right: 40px; bottom: 40px;
    text-align: right; color: var(--ink-soft);
    font-style: normal;
    font-weight: 300; font-size: 13px; line-height: 19px;
  }

  .card--brand {
    display: flex; align-items: center; justify-content: center;
  }
  .card--brand .wordmark { font-size: 32px; }
</style>
</head>
<body>
<main class="sheet">

  <section class="card card--contact" aria-label="Business card, contact side">
    <div class="wordmark">Halvren Tax Advisers</div>

    <div class="identity">
      <h1 class="identity__name">Martin G. Pellow, MST, CPA, PFS</h1>
      <div class="identity__row">
        <p class="identity__title">Managing Director, Tax</p>
        <span class="identity__rule"></span>
      </div>
    </div>

    <ul class="contacts">
      <li>
        <svg viewBox="0 0 16 16" aria-hidden="true"><path d="M4 1h8a1 1 0 0 1 1 1v12a1 1 0 0 1-1 1H4a1 1 0 0 1-1-1V2a1 1 0 0 1 1-1zm.5 1.5v9h7v-9zm3.5 10a.75.75 0 1 0 0 1.5.75.75 0 0 0 0-1.5z"/></svg>
        (505) 555-0132
      </li>
      <li>
        <svg viewBox="0 0 16 16" aria-hidden="true"><path d="M3.6 1.2l2.2 2.6-1.3 1.7a9 9 0 0 0 6 6l1.7-1.3 2.6 2.2-1.3 2.4C7 14.6 1.4 9 1.2 2.5z"/></svg>
        (575) 555-0187
      </li>
      <li>
        <svg viewBox="0 0 16 16" aria-hidden="true"><path d="M1 5c2-3 12-3 14 0l-1 2-3-1V4.5H5V6L2 7zM4 8h8l2 6H2z"/></svg>
        (575) 555-0149
      </li>
      <li>
        <svg viewBox="0 0 16 16" aria-hidden="true"><path d="M1 3h14v10H1zm1.5 1.3v.4L8 8.6l5.5-3.9v-.4zm0 2.2v5h11v-5L8 10.4z"/></svg>
        mpellow@myhalvrenfirm.net
      </li>
      <li>
        <svg viewBox="0 0 16 16" aria-hidden="true"><path d="M8 1a7 7 0 1 0 0 14A7 7 0 0 0 8 1zm0 1.5c.8 0 1.8 1.6 2.2 4H5.8C6.2 4.1 7.2 2.5 8 2.5zM2.6 8h2.9c0 .5 0 1 .1 1.5H2.8A5.6 5.6 0 0 1 2.6 8zm7.9 0h2.9c0 .5-.1 1-.2 1.5h-2.8c.1-.5.1-1 .1-1.5zM7 8h2l-.1 1.5H7.1zm-3.6 3h2.4c.2.9.5 1.7.9 2.3A5.5 5.5 0 0 1 3.4 11zm3.9 0h1.4c-.2.9-.5 1.6-.7 2-.2-.4-.5-1.1-.7-2zm2.9 0h2.4a5.5 5.5 0 0 1-3.3 2.3c.4-.6.7-1.4.9-2.3z"/></svg>
        www.halvrenfirm-example.tax
      </li>
    </ul>

    <address class="address">
      3807 Fenwick Rd., Suite 118<br>
      Marlow Springs, NM 87199
    </address>
  </section>

  <section class="card card--brand" aria-label="Business card, brand side">
    <div class="wordmark">Halvren Tax Advisers</div>
  </section>

</main>
</body>
</html>
```